vermalo web design

- Company / Site Description
We are developing a website that will allow anyone in Europe to find in one click, cultural things to do (Exhibition, Museum, Monument, Zoo, Aquarium, Archaeological site…) with friends or family, and to organize the visit (book a ticket / a private visit, book a restaurant nearby…).

Examples
1. You're in London with your girlfriend, it's saturday 10 am, you have two hours to spend and you want to see an exhibition. We provide you in one click all the exhibition matching your location / time and date.

2. You're in Berlin with some friends, it's thursday night you want to go out, but you don't know what to do. We provide you a list of experience, you can select for instance "I want to be on top of the world", and we show you a list of venues matching the selected experience / date / time /location of your request.

- Brand name : Vermalo
- Activity : Cultural Leisure, cultural entertainment

- Target audience
Broad target will be between 20 and 55. Core target will be between 25 and 40. Most likely to live in a city and in Europe.

- Behaviours and preferences
Our user is under time constraint (few minutes to find and choose his visit), idea constraint (is not sure about what to do and see) and money constraint.
He wants to have an easy to use website, not cluttered with information, focussed on added value information. He wants to have a website which is modern, fun and elegant that he will deem as professional and trustworthy.

- Our expectations (Do’s and Don’t)
We want to move away from traditional design. We want some OUT OF THE BOX design. Think of a website design that will look like an app design.
We want to make an awesome / extra ordinary /remember-able design. The design must be so cool, that the user wants to come back to the site. In two words: THINK EXTRAORDINARY.
You can use photos to help the user understand functions. If you use photo, use creative commons license photo.
Avoid black colors

- Functional Requirements
We need Four pages:
1. Home Page (desktop and mobile version): it’s both the homepage and the assistant page. This page will allow the user to find in one click his visit (please refer to the pdf file Assistant home page). The page must be self-explanatory for a first time user.
2. Assistant result page (desktop version): it’s the page that display the results found by the assistant based on the criteria search (please refer to the pdf file mockup - Assistant result page)
3. Site / Event page (desktop version): it’s the page that display each result information (please refer to the pdf file mockup – Event / Site Page)
The pdf files list all the elements include in each page + gives you a mockup of each page (just to put in perspective the element required). You are completely free about the design.
We don’t have the logo yet. Use a dummy logo for your page design.
The selected winner can expect to work with us immediately after the contest and on a on a regular basis later on.

- Technical Requirements
No Flash
For the winner, we will manage the CSS you will just need to provide :
. One PSD file containing all the pages
. Inside the PSD file we want for each page two groups: the first group will embed the desktop design, the second group will embed the responsive mobile design (Home Page only).
In total there should be 4 groups inside the PSD file (3 desktop groups, 1 mobile group).
Each group must contain all the elements specified in the pdf file

Website we like
http://demo.plandorix.example/?theme=Velunt
http://rosabel.quintorhub.example/#home
http://blogsite.fenk.daltoroute.example/2/
http://demo.plandorix.example/?theme=Mosaru
http://www.quarnivo.example/themes/lumbe/
http://gridmarket.example/item/tav-responsive-photography-blog-theme/full_screen_preview/8146027
http://items.zkvortel.example/?product=example
http://uk.harnoway.example

Reason: Due to the request of several designers, we have agreed to add 7 additional days to the contest deadline. Thank you. The vermalo team

Reason: We still need to collect all the votes. Sorry for the delay.

Reason: Hello, We extend the contest deadline, in order to collect all the votes from the poll. We should have everything finalized by sunday. Thank you vermalo team

```html
<!DOCTYPE html>
<html lang="en">
<head>
<meta charset="utf-8">
<title>vermalo – cultural assistant</title>
<link rel="stylesheet" href="https://fonts.googleapis.com/css2?family=Questrial&family=Didact+Gothic&display=swap">
<style>
  :root {
    --page-bg: #ececec;
    --city-dark: #8f8a84;
    --city-mid: #b3a488;
    --city-warm: #d2b07a;
    --panel-veil: rgba(205, 200, 192, 0.42);
    --white: #ffffff;
    --ink: #2b2b2b;
    --ink-soft: #4a4a4a;
    --tile-arts: #1fe3a5;
    --tile-cinema: #16e9f0;
    --tile-wine: #f1184b;
    --tile-dining: #fbd52b;
    --tile-musicals: #f5654a;
    --card-gallery: #1fe0a8;
    --card-museum: #1aa3f0;
    --card-hall: #f7a04a;
    --card-park: #b02ab8;
    --tag-bar: #d9d9d9;
    --glass: rgba(120, 112, 104, 0.38);
    --glass-strong: rgba(90, 84, 78, 0.45);
    --social-box: rgba(80, 78, 76, 0.62);
  }
  * { box-sizing: border-box; margin: 0; padding: 0; }
  html, body {
    width: 1200px; height: 995px; overflow: hidden;
    background: var(--page-bg);
    font-family: "Questrial", "Didact Gothic", sans-serif;
  }
  .stage {
    position: absolute; left: 0; top: 160px;
    width: 1092px; height: 615px;
    transform: scale(1.0989); transform-origin: 0 0;
    overflow: hidden;
  }
  .city-backdrop {
    position: absolute; inset: 0;
    background:
      radial-gradient(ellipse at 88% 30%, rgba(240, 200, 130, 0.75), transparent 60%),
      linear-gradient(100deg, var(--city-dark) 0%, var(--city-mid) 45%, var(--city-warm) 100%);
  }
  .side-panel {
    position: absolute; left: 0; top: 0; width: 358px; height: 615px;
    background: var(--panel-veil);
    border-right: 1px solid rgba(255,255,255,0.25);
  }
  .brand {
    position: absolute; left: 160px; top: 38px;
    color: var(--white); font-size: 20px; letter-spacing: 1px;
  }
  .list-tabs {
    position: absolute; left: 158px; top: 174px; width: 185px;
    display: flex; justify-content: space-between; color: var(--white); font-size: 12.5px;
  }
  .list-tabs .active { font-weight: bold; font-family: "Didact Gothic", sans-serif; }
  .list-tabs .sep { font-weight: bold; }
  .list-tabs .muted { opacity: 0.8; }

  .venue-card { position: absolute; left: 158px; width: 185px; height: 68px; }
  .venue-card .info { position: absolute; left: 0; top: 0; width: 112px; height: 58px; padding: 4px 4px; }
  .venue-card .photo { position: absolute; left: 112px; top: 0; width: 73px; height: 58px; }
  .venue-card .title { font-size: 10px; color: var(--ink); line-height: 1.05; }
  .venue-card .blurb { font-size: 6.5px; color: var(--white); font-weight: bold; line-height: 1.25; margin-top: 6px; }
  .venue-card .tags {
    position: absolute; left: 0; top: 58px; width: 185px; height: 10px;
    background: var(--tag-bar); font-size: 6px; color: var(--ink-soft); padding: 1.5px 3px;
    white-space: nowrap; overflow: hidden;
  }
  .venue-card .tags b { color: var(--card-museum); }
  .venue-card .fav { position: absolute; left: 140px; top: 4px; width: 20px; height: 20px; }
  .card-gallery { top: 200px; } .card-gallery .info { background: var(--card-gallery); }
  .card-gallery .photo { background: linear-gradient(135deg, #3a3a3a, #cfcfcf 60%, #777); }
  .card-museum { top: 281px; } .card-museum .info { background: var(--card-museum); }
  .card-museum .photo { background: linear-gradient(135deg, #555, #bdbdbd 55%, #444); }
  .card-hall { top: 361px; } .card-hall .info { background: var(--card-hall); }
  .card-hall .photo { background: linear-gradient(180deg, #4a8ad8, #c9874a 60%, #8a4a2a); }
  .card-park { top: 442px; height: 38px; overflow: hidden; opacity: 0.8; }
  .card-park .info { background: var(--card-park); }
  .card-park .photo { background: linear-gradient(135deg, #333, #aaa); }
  .more-fade {
    position: absolute; left: 158px; top: 462px; width: 185px; height: 20px;
    background: linear-gradient(transparent, rgba(190,184,176,0.9));
    border-bottom: 1px solid rgba(255,255,255,0.5);
  }
  .more-label { position: absolute; left: 238px; top: 470px; font-size: 8px; color: var(--white); font-weight: bold; }
  .more-arrow { position: absolute; left: 241px; top: 481px; }

  .user-bar { position: absolute; left: 640px; top: 68px; width: 200px; height: 80px; color: var(--white); }
  .weather-icon { position: absolute; left: 78px; top: 12px; }
  .gear { position: absolute; left: 118px; top: 3px; }
  .weather-text { position: absolute; left: 68px; top: 32px; font-size: 6.5px; text-align: center; line-height: 1.1; }
  .weather-text b { font-size: 7px; }
  .search {
    position: absolute; left: 3px; top: 49px; width: 115px; height: 11px;
    background: var(--white); border-radius: 6px; font-size: 6.5px; color: var(--ink); padding: 1px 8px;
  }
  .avatar {
    position: absolute; left: 125px; top: 4px; width: 56px; height: 56px;
    border: 1.5px solid var(--white); border-radius: 50%;
  }
  .avatar .placeholder {
    position: absolute; left: 6px; top: 6px; width: 41px; height: 41px; border-radius: 50%;
    background: rgba(255,255,255,0.55);
  }
  .greeting { position: absolute; left: 132px; top: 62px; width: 42px; text-align: center; font-size: 7px; line-height: 1.1; }
  .greeting span { opacity: 0.8; }

  .interest-grid { position: absolute; left: 375px; top: 200px; width: 377px; height: 112px; }
  .interest {
    position: absolute; height: 56px; font-size: 13px; color: var(--ink);
    padding: 21px 0 0 18px; white-space: nowrap;
  }
  .interest .remove { position: absolute; top: 4px; width: 20px; height: 20px; }
  .tile-arts { left: 0; top: 0; width: 112px; background: var(--tile-arts); }
  .tile-cinema { left: 112px; top: 0; width: 137px; background: var(--tile-cinema); padding-left: 12px; }
  .tile-wine { left: 249px; top: 0; width: 128px; background: var(--tile-wine); }
  .tile-dining { left: 0; top: 56px; width: 127px; background: var(--tile-dining); }
  .tile-musicals { left: 127px; top: 56px; width: 105px; background: var(--tile-musicals); padding-left: 20px; }
  .tile-suggest {
    left: 232px; top: 56px; width: 113px; color: rgba(255,255,255,0.8);
    border: 1px solid rgba(255,255,255,0.5); font-size: 14px;
  }

  .when-where { position: absolute; left: 375px; top: 322px; color: var(--white); }
  .date-line {
    position: absolute; left: 0; top: 0; width: 205px; height: 20px;
    background: var(--glass); font-size: 14px; padding: 1px 5px; white-space: nowrap;
  }
  .edit-btn {
    position: absolute; left: 211px; top: 0; width: 48px; height: 22px;
    border: 1px solid rgba(255,255,255,0.85); font-size: 9px; font-weight: bold;
    text-align: center; padding-top: 5px; font-family: "Didact Gothic", sans-serif;
  }
  .time-box {
    position: absolute; left: 0; top: 22px; width: 168px; height: 40px; background: var(--glass-strong);
  }
  .time { position: absolute; left: 6px; top: 7px; font-size: 20px; }
  .city { position: absolute; left: 98px; top: 3px; font-size: 13px; font-weight: bold; font-family: "Didact Gothic", sans-serif; }
  .country { position: absolute; left: 117px; top: 20px; font-size: 9px; opacity: 0.85; }

  .close-toggle { position: absolute; left: 559px; top: 383px; font-size: 7px; color: var(--white); font-weight: bold; }
  .close-arrow { position: absolute; left: 562px; top: 393px; }
  .site-footer {
    position: absolute; left: 375px; top: 396px; width: 383px; height: 84px;
    background: rgba(140, 134, 126, 0.45); color: var(--white); font-size: 7px;
  }
  .footer-col { position: absolute; top: 13px; line-height: 1.45; }
  .footer-col h4 { font-weight: normal; font-size: 6.5px; letter-spacing: 0.3px; margin-bottom: 3px; }
  .footer-col li { list-style: none; }
  .col-language { left: 10px; }
  .col-language .langs { position: absolute; left: 48px; top: 0; }
  .col-language .langs li:first-child { font-weight: bold; }
  .col-account { left: 128px; }
  .col-follow { left: 215px; }
  .col-about { left: 286px; }

  .social-rail { position: absolute; left: 1020px; top: 421px; width: 42px; }
  .social-link {
    display: block; width: 42px; height: 42px; background: var(--social-box);
    border-bottom: 1px solid rgba(255,255,255,0.15);
    color: var(--white); font-size: 6.5px; text-align: center; padding-top: 17px;
  }
</style>
</head>
<body>
<main class="stage">
  <div class="city-backdrop" role="img" aria-label="Warm sunset photograph of a city skyline with tall towers"></div>

  <aside class="side-panel">
    <div class="brand">vermalo</div>
    <nav class="list-tabs"><span class="active">Recommended</span><span class="sep">|</span><span class="muted">Favorites</span></nav>

    <article class="venue-card card-gallery">
      <div class="info"><p class="title">Marlow Gallery</p><p class="blurb">Lorem ipsum dolor sit amet, consectetur adipiscing elit. Proin nec quam non ante...</p></div>
      <div class="photo" role="img" aria-label="Photo of a gallery hall interior"></div>
      <svg class="fav" viewBox="0 0 20 20"><circle cx="10" cy="10" r="8.5" fill="none" stroke="#111" stroke-width="2"/><path d="M10 14.5 5.6 10a2.4 2.4 0 0 1 4.4-3 2.4 2.4 0 0 1 4.4 3Z" fill="#111"/></svg>
      <p class="tags"><b>Tags:</b> Gallery, Arts, Contemporary, Museum...</p>
    </article>

    <article class="venue-card card-museum">
      <div class="info"><p class="title">Museum of<br>Earth Science</p><p class="blurb" style="margin-top:2px">Lorem ipsum dolor sit amet, consectetur adipiscing elit. Proin nec quam non ante...</p></div>
      <div class="photo" role="img" aria-label="Photo of a museum main hall"></div>
      <svg class="fav" viewBox="0 0 20 20"><circle cx="10" cy="10" r="8.5" fill="none" stroke="#111" stroke-width="2"/><path d="M10 14.5 5.6 10a2.4 2.4 0 0 1 4.4-3 2.4 2.4 0 0 1 4.4 3Z" fill="#111"/></svg>
      <p class="tags"><b>Tags:</b> Museum, History, Anthropology...</p>
    </article>

    <article class="venue-card card-hall">
      <div class="info"><p class="title">Royal Orwin Hall</p><p class="blurb">Lorem ipsum dolor sit amet, consectetur adipiscing elit. Proin nec quam non ante...</p></div>
      <div class="photo" role="img" aria-label="Photo of a domed concert hall at dusk"></div>
      <svg class="fav" viewBox="0 0 20 20"><circle cx="10" cy="10" r="8.5" fill="none" stroke="#111" stroke-width="2"/><path d="M10 14.5 5.6 10a2.4 2.4 0 0 1 4.4-3 2.4 2.4 0 0 1 4.4 3Z" fill="#111"/></svg>
      <p class="tags"><b>Tags:</b> Music, Classical Music, Concerts...</p>
    </article>

    <article class="venue-card card-park">
      <div class="info"><p class="title">Kestle Park</p></div>
      <div class="photo" role="img" aria-label="Photo of a city park"></div>
      <svg class="fav" viewBox="0 0 20 20"><circle cx="10" cy="10" r="8.5" fill="none" stroke="#111" stroke-width="2"/><path d="M10 14.5 5.6 10a2.4 2.4 0 0 1 4.4-3 2.4 2.4 0 0 1 4.4 3Z" fill="#111"/></svg>
    </article>
    <div class="more-fade"></div>
    <span class="more-label">More</span>
    <svg class="more-arrow" width="14" height="7" viewBox="0 0 14 7"><path d="M0 0 7 7 14 0" fill="none" stroke="#fff" stroke-width="1"/></svg>
  </aside>

  <header class="user-bar">
    <svg class="weather-icon" width="20" height="18" viewBox="0 0 20 18"><path d="M5 10a4 4 0 0 1 1-7.8A5 5 0 0 1 15 4a3 3 0 0 1 0 6Z" fill="none" stroke="#fff" stroke-width="1.2"/><path d="M6 13l-1 3M10 13l-1 3M14 13l-1 3" stroke="#fff" stroke-width="1.2"/></svg>
    <svg class="gear" width="12" height="12" viewBox="0 0 12 12"><circle cx="6" cy="6" r="3.2" fill="none" stroke="#fff" stroke-width="2"/><path d="M6 0v2.5M6 9.5V12M0 6h2.5M9.5 6H12M1.8 1.8l1.8 1.8M8.4 8.4l1.8 1.8M1.8 10.2l1.8-1.8M8.4 3.6l1.8-1.8" stroke="#fff" stroke-width="1.6"/></svg>
    <p class="weather-text"><b>8 celsius</b><br>Rain, Wind</p>
    <div class="search">Search.....</div>
    <div class="avatar"><div class="placeholder" role="img" aria-label="User profile picture"></div></div>
    <p class="greeting"><b>Hello</b><br><span>Tomas</span></p>
  </header>

  <section class="interest-grid">
    <div class="interest tile-arts">Visual Arts<svg class="remove" style="left:86px" viewBox="0 0 20 20"><circle cx="10" cy="10" r="8.5" fill="none" stroke="#111" stroke-width="1.8"/><path d="M7.5 7.5l5 5M12.5 7.5l-5 5" stroke="#111" stroke-width="1"/></svg></div>
    <div class="interest tile-cinema">Foreign Cinema<svg class="remove" style="left:110px" viewBox="0 0 20 20"><circle cx="10" cy="10" r="8.5" fill="none" stroke="#111" stroke-width="1.8"/><path d="M7.5 7.5l5 5M12.5 7.5l-5 5" stroke="#111" stroke-width="1"/></svg></div>
    <div class="interest tile-wine">Wine Tasting<svg class="remove" style="left:101px" viewBox="0 0 20 20"><circle cx="10" cy="10" r="8.5" fill="none" stroke="#111" stroke-width="1.8"/><path d="M7.5 7.5l5 5M12.5 7.5l-5 5" stroke="#111" stroke-width="1"/></svg></div>
    <div class="interest tile-dining">Fine Dining<svg class="remove" style="left:101px" viewBox="0 0 20 20"><circle cx="10" cy="10" r="8.5" fill="none" stroke="#111" stroke-width="1.8"/><path d="M7.5 7.5l5 5M12.5 7.5l-5 5" stroke="#111" stroke-width="1"/></svg></div>
    <div class="interest tile-musicals">Musicals<svg class="remove" style="left:79px" viewBox="0 0 20 20"><circle cx="10" cy="10" r="8.5" fill="none" stroke="#111" stroke-width="1.8"/><path d="M7.5 7.5l5 5M12.5 7.5l-5 5" stroke="#111" stroke-width="1"/></svg></div>
    <div class="interest tile-suggest">You want?</div>
  </section>

  <section class="when-where">
    <div class="date-line">Saturday, 14th of December</div>
    <div class="edit-btn">Edit</div>
    <div class="time-box"><span class="time">6:00pm</span><span class="city">London</span><span class="country">(UK)</span></div>
  </section>

  <span class="close-toggle">close</span>
  <svg class="close-arrow" width="14" height="7" viewBox="0 0 14 7"><path d="M0 0 7 7 14 0" fill="none" stroke="#fff" stroke-width="1"/></svg>

  <footer class="site-footer">
    <div class="footer-col col-language"><h4>LANGUAGE</h4><ul class="langs"><li>English</li><li>Francais</li></ul></div>
    <div class="footer-col col-account"><h4>YOU AND POCKET</h4><ul><li>Contact us</li><li>Personal data</li><li>Legal mention</li></ul></div>
    <div class="footer-col col-follow"><h4>FOLLOW US</h4><ul><li>Pagenest</li><li>Chirpline</li><li>Orbitly</li></ul></div>
    <div class="footer-col col-about"><h4>ABOUT US</h4><ul><li>Presentation</li><li>The Team</li></ul></div>
  </footer>

  <nav class="social-rail">
    <a class="social-link">Pagenest</a>
    <a class="social-link">Snapfold</a>
    <a class="social-link">Chirpline</a>
    <a class="social-link">Orbitly</a>
  </nav>
</main>
</body>
</html>
```